Business Card Design

Harlow Sun and Electrical is a new company that specializes in solar pv. I need a card with similar attributes to the ones I have attached. I am after a two sided card with the logo on one side and the logo plus info on the other. I would prefer one side to be black and the other to be a colour but am open to suggestions. The colour scheme I was thinking of was blue or green. I plan on spot glossing the logos if that makes any difference. I have attached a file of my logo in a few colours, none of which I am completely sold on so please feel free to change colous to suit.
Thanks.
Contact Information for Business Card
Dorian Harlow, www.hwx-example.net.nz, dorian@hwx-example.net.nz, t. 0508 4 BRIGHT m. 027469318

```html
<!DOCTYPE html>
<html lang="en">
<head>
<meta charset="utf-8">
<title>Harlow Sun and Electrical — Business Card</title>
<link href="https://fonts.googleapis.com/css2?family=Michroma&family=Questrial&display=swap" rel="stylesheet">
<style>
  :root {
    --card-black: #000000;
    --electric-blue: #06bdf5;
    --name-steel: #8fb4c9;
  }
  html, body {
    margin: 0;
    padding: 0;
    width: 1200px;
    height: 900px;
    overflow: hidden;
    background: var(--card-black);
  }
  .card {
    position: relative;
    width: 1200px;
    height: 900px;
    background: var(--card-black);
  }
  .brand {
    position: absolute;
    left: 145px;
    top: 300px;
    width: 400px;
    display: flex;
    flex-direction: column;
    align-items: center;
  }
  .brand-mark {
    width: 132px;
    height: 132px;
    background: var(--electric-blue);
  }
  .brand-name {
    margin-top: 34px;
    font-family: "Questrial", sans-serif;
    font-size: 21px;
    letter-spacing: 0.3px;
    text-transform: uppercase;
    color: var(--name-steel);
    white-space: nowrap;
  }
  .divider {
    position: absolute;
    left: 577px;
    top: 255px;
    width: 2px;
    height: 322px;
    background: var(--electric-blue);
  }
  .contact {
    position: absolute;
    left: 636px;
    top: 338px;
    margin: 0;
    font-family: "Michroma", sans-serif;
    color: var(--electric-blue);
    white-space: nowrap;
  }
  .contact-name {
    display: block;
    font-size: 26px;
    line-height: 34px;
    letter-spacing: 2px;
    text-transform: uppercase;
  }
  .contact-line {
    display: block;
    font-size: 21px;
    line-height: 34px;
    letter-spacing: 1.5px;
  }
  .contact-line a {
    color: inherit;
    text-decoration: none;
  }
</style>
</head>
<body>
  <main class="card">
    <section class="brand">
      <div class="brand-mark" aria-hidden="true"></div>
      <div class="brand-name">Harlow Sun and Electrical</div>
    </section>

    <div class="divider" aria-hidden="true"></div>

    <address class="contact">
      <span class="contact-name">Dorian Harlow</span>
      <span class="contact-line"><a href="http://www.hwx-example.net.nz">www.hwx-example.net.nz</a></span>
      <span class="contact-line"><a href="mailto:dorian@hwx-example.net.nz">dorian@hwx-example.net.nz</a></span>
      <span class="contact-line">t. 05084274448</span>
      <span class="contact-line">m. 027469318</span>
    </address>
  </main>
</body>
</html>
```